Creative & Appealing Business Card

Required a business card for Vantrelink
We specialise in claims management services for PPI ( Payment Protection Insurance.
2 sided business card
Round Corners
I like embossed and raised lettering

```html
<!DOCTYPE html>
<html lang="en">
<head>
<meta charset="utf-8">
<title>Vantrelink Business Card</title>
<link href="https://fonts.googleapis.com/css2?family=Lato:wght@400;700&display=swap" rel="stylesheet">
<style>
  :root {
    --ink: #1b2a30;
    --slate: #3e545c;
    --paper: #ffffff;
    --backdrop: #e7e9ea;
    --rule: #5b6a70;
  }
  html, body {
    margin: 0;
    width: 1200px;
    height: 800px;
    overflow: hidden;
    background: var(--backdrop);
    font-family: "Lato", sans-serif;
  }
  .canvas {
    width: 1200px;
    height: 800px;
    display: flex;
    align-items: center;
    justify-content: center;
    gap: 40px;
  }
  .card {
    position: relative;
    width: 540px;
    height: 310px;
    border-radius: 18px;
    overflow: hidden;
    box-shadow: 0 6px 18px rgba(0,0,0,0.18);
  }
  /* Front */
  .card--front { background: var(--paper); color: var(--ink); }
  .front-waves { position: absolute; inset: 0; }
  .brand-block {
    position: absolute;
    left: 40px;
    top: 62px;
    width: 210px;
    text-align: center;
  }
  .brand-dot {
    width: 46px; height: 46px;
    border-radius: 50%;
    background: var(--ink);
    margin: 0 auto 10px;
  }
  .brand-name {
    font-size: 27px;
    font-weight: 400;
    letter-spacing: 1px;
    color: var(--slate);
    margin: 0;
  }
  .brand-address {
    font-size: 12.5px;
    font-weight: 700;
    color: var(--ink);
    margin: 8px 0 0;
    white-space: nowrap;
  }
  .divider {
    position: absolute;
    left: 0; top: 0;
  }
  .contact-block {
    position: absolute;
    left: 300px;
    top: 80px;
  }
  .person-name {
    font-size: 16px;
    font-weight: 700;
    letter-spacing: 1px;
    margin: 0 0 12px;
  }
  .contact-list { list-style: none; margin: 0; padding: 0; }
  .contact-list li {
    display: flex;
    align-items: center;
    gap: 12px;
    font-size: 16px;
    font-weight: 700;
    color: var(--slate);
    line-height: 24px;
  }
  .contact-icon { width: 16px; height: 14px; flex: none; }
  /* Back */
  .card--back { background: var(--ink); color: var(--paper); }
  .back-brand {
    position: absolute;
    left: 0; right: 0;
    top: 86px;
    display: flex;
    justify-content: center;
    align-items: center;
    gap: 12px;
    padding-left: 110px;
  }
  .back-brand .brand-dot { background: var(--paper); margin: 0; width: 40px; height: 40px; }
  .back-brand .brand-name { color: var(--paper); font-size: 22px; }
  .services {
    position: absolute;
    left: 130px;
    top: 170px;
    font-size: 12.5px;
    letter-spacing: 0.5px;
    line-height: 1.35;
    text-transform: uppercase;
  }
  .services p { margin: 0; }
  .services .lead { margin-bottom: 10px; }
</style>
</head>
<body>
<main class="canvas">

  <section class="card card--front" aria-label="Card front">
    <svg class="front-waves" width="540" height="310" viewBox="0 0 540 310">
      <path d="M0 180 C110 150 230 170 320 225 C400 272 470 270 540 240 L540 310 L0 310 Z" fill="var(--slate)"/>
      <path d="M0 192 C110 165 230 185 320 240 C400 286 470 284 540 256 L540 310 L0 310 Z" fill="var(--paper)"/>
      <path d="M0 198 C110 172 230 192 320 247 C400 292 470 292 540 266 L540 310 L0 310 Z" fill="var(--ink)"/>
      <path d="M190 205 C260 225 300 250 330 262 C390 286 460 292 540 276 L540 284 C460 300 390 296 325 270 C290 255 250 232 190 205 Z" fill="var(--paper)"/>
    </svg>
    <svg class="divider" width="540" height="310">
      <line x1="276" y1="85" x2="262" y2="225" stroke="var(--rule)" stroke-width="1.2"/>
    </svg>

    <div class="brand-block">
      <div class="brand-dot"></div>
      <h1 class="brand-name">VANTRELINK</h1>
      <p class="brand-address">48 Marlow Street, London, N4 2QT</p>
    </div>

    <div class="contact-block">
      <h2 class="person-name">DANIEL OKAFOR</h2>
      <ul class="contact-list">
        <li>
          <svg class="contact-icon" viewBox="0 0 16 14"><rect x="1" y="2" width="14" height="10" fill="var(--ink)"/><path d="M1 2 L8 8 L15 2" stroke="#fff" fill="none" stroke-width="1.2"/></svg>
          daniel@vantrelink.com
        </li>
        <li>
          <svg class="contact-icon" viewBox="0 0 16 14"><path d="M3 1 L6 1 L7 4 L5.5 5.5 C6.5 7.5 8 9 10 10 L11.5 8.5 L14 9.5 L14 12.5 C8 13 2 7 3 1 Z" fill="var(--ink)"/></svg>
          +44 (0) 300 555 0142
        </li>
        <li>
          <svg class="contact-icon" viewBox="0 0 16 14"><rect x="4" y="0.5" width="8" height="4" fill="var(--ink)"/><rect x="1" y="5" width="14" height="6" rx="1" fill="var(--ink)"/><rect x="4" y="9" width="8" height="4.5" fill="var(--ink)" stroke="#fff" stroke-width="0.8"/></svg>
          +44 (0) 207 946 0318
        </li>
        <li>
          <svg class="contact-icon" viewBox="0 0 16 14"><rect x="1.5" y="1" width="13" height="9" fill="none" stroke="var(--ink)" stroke-width="1.4"/><rect x="6" y="10" width="4" height="2" fill="var(--ink)"/><rect x="4" y="12" width="8" height="1.4" fill="var(--ink)"/></svg>
          www.vantrelink.com
        </li>
      </ul>
    </div>
  </section>

  <section class="card card--back" aria-label="Card back">
    <div class="back-brand">
      <div class="brand-dot"></div>
      <span class="brand-name">VANTRELINK</span>
    </div>
    <div class="services">
      <p class="lead">Claims management service for mis-sold</p>
      <p>Payment protection insurance claims</p>
      <p>Interest rate hedging products / swaps</p>
    </div>
  </section>

</main>
</body>
</html>
```